Business card and stationary package

Travel management company looking for designs for single sided business cards, letterhead and envelope. Looking for contemporary designs using our existing logo. Design should clean, not trendy, no gradation of colors and no graphic other than the icon from the logo. Nothing complicated or difficult to read. Should be a crisp design using blue, gray and black colors only.
Letterhead should include a Word template and PDF template.
Business cards are one sided as the reverse will be dynamic images in our company portfolio of images.
We will use the same designer periodically for design projects using the same style guide for upcoming projects as well. Prefer working with designer that will assist with website, brochures and other marketing materials.

Logo Colors and Font:
Blue: 2189c6 Color Hex
Gray: 666666 Color Hex 60% Black
Black: 100% Black
Font: Century Gothic

Target Market(s)

business-to-business

Industry/Entity Type

Travel Industry

Contact Information for Business Card

Sample information for business cards will be:

Daniel Fenwick
Managing Partner

Harborline Journey Services, Inc.
274 Alder Lane, Suite 3621
Calder Falls, ME 04990

207-555-0148 Direct Dial
207-555-0193 Fax

daniel@harborlinejourney.net
www.harborlinejourney.net

Font styles to use
Sans Serif

Requirements
Must have
• Clean, crisp design, easy to ready, memorable.
Nice to have
• We tend to like dynamic designs that are simple, not trendy, contemporary and easy to read.
Should not have
• no gradation of colors and no graphic other than the icon from the logo, no background images
• **Note that the background should only be white. No black/gary backgrounds or graded colors**

```html
<!DOCTYPE html>
<html lang="en">
<head>
<meta charset="utf-8">
<title>Harborline Journey Services – Stationery Set</title>
<link href="https://fonts.googleapis.com/css2?family=Questrial&display=swap" rel="stylesheet">
<style>
  :root{
    --blue:#2e82b6;
    --gray:#666666;
    --black:#000000;
    --paper:#ffffff;
    --ground:#eceeef;
    --edge:#dcdfe1;
  }
  *{margin:0;padding:0;box-sizing:border-box}
  html,body{width:1200px;height:795px;overflow:hidden}
  body{background:var(--ground);font-family:"Questrial",sans-serif;color:var(--gray);position:relative}
  .piece{position:absolute;background:var(--paper);border:1px solid var(--edge)}

  .brand{display:flex;align-items:center;gap:4px;color:var(--blue);letter-spacing:.04em;white-space:nowrap}
  .brand-dot{border-radius:50%;background:var(--blue);flex:none}
  .brand--light{color:var(--paper)}
  .brand--light .brand-dot{background:var(--paper)}

  /* Letterhead */
  .letterhead{left:292px;top:99px;width:294px;height:414px}
  .letterhead .brand{position:absolute;left:110px;top:22px;font-size:10px}
  .letterhead .brand-dot{width:9px;height:9px}
  .letterhead-footer{position:absolute;left:0;right:0;top:389px;text-align:center;font-size:4.6px;line-height:7.5px;color:var(--gray);white-space:nowrap}
  .letterhead-footer strong{font-weight:400;color:var(--black)}
  .letterhead-footer .ico{color:var(--blue)}

  /* Folder */
  .folder{left:636px;top:80px;width:346px;height:437px;background:var(--blue);border-color:var(--blue)}
  .folder-spine{position:absolute;left:8px;top:0;bottom:0;width:1px;background:rgba(0,0,0,.12)}
  .folder .brand{position:absolute;left:0;right:0;top:200px;justify-content:center;font-size:30px;gap:12px;letter-spacing:.05em}
  .folder .brand-dot{width:22px;height:22px}

  /* Business cards */
  .card{width:131px;height:75px}
  .card-front{left:187px;top:550px}
  .card-front .brand{position:absolute;left:10px;top:32px;font-size:7.5px;gap:3px}
  .card-front .brand-dot{width:7px;height:7px}
  .card-divider{position:absolute;left:69px;top:13px;width:1px;height:52px;background:var(--edge)}
  .card-details{position:absolute;left:74px;top:14px;font-size:3.6px;line-height:4.6px;color:var(--gray);white-space:nowrap}
  .card-name{font-size:5px;line-height:5.6px;color:var(--blue)}
  .card-title{margin-bottom:2.5px}
  .card-company{color:var(--black)}
  .card-gap{height:2px}
  .card-back{left:187px;top:648px;height:74px;background:var(--blue);border-color:var(--blue)}
  .card-back .brand{position:absolute;left:0;right:0;top:31px;justify-content:center;font-size:9px}
  .card-back .brand-dot{width:8px;height:8px}

  /* Envelopes */
  .envelope{top:562px;width:327px;height:156px}
  .envelope-front{left:354px}
  .envelope-front .brand{position:absolute;left:15px;top:22px;font-size:10px}
  .envelope-front .brand-dot{width:9px;height:9px}
  .return-address{position:absolute;left:39px;top:38px;font-size:4.6px;line-height:5.8px;color:var(--gray);font-style:normal}
  .return-address .company{color:var(--black)}
  .envelope-back{left:714px}
  .envelope-flap{position:absolute;left:0;top:0;width:100%;height:56px}
  .envelope-back .brand{position:absolute;left:0;right:0;top:12px;justify-content:center;font-size:8px}
  .envelope-back .brand-dot{width:7px;height:7px}
  .flap-url{position:absolute;left:0;right:0;top:38px;text-align:center;font-size:4.4px;letter-spacing:.12em;color:var(--paper)}
</style>
</head>
<body>

  <section class="piece letterhead" aria-label="Letterhead">
    <div class="brand"><span class="brand-dot"></span>HARBORLINE</div>
    <footer class="letterhead-footer">
      <p><strong>Harborline Journey Services, Inc.</strong> | 274 Alder Lane, Suite 3621, Calder Falls, ME 04990</p>
      <p><span class="ico">&#9742;</span> 207-555-0148 (Direct) <span class="ico">&#9632;</span> 207-555-0193 <span class="ico">&#9993;</span> daniel@harborlinejourney.net <span class="ico">&#9679;</span> harborlinejourney.net</p>
    </footer>
  </section>

  <section class="piece folder" aria-label="Presentation folder">
    <span class="folder-spine"></span>
    <div class="brand brand--light"><span class="brand-dot"></span>HARBORLINE</div>
  </section>

  <section class="piece card card-front" aria-label="Business card, front">
    <div class="brand"><span class="brand-dot"></span>HARBORLINE</div>
    <span class="card-divider"></span>
    <div class="card-details">
      <p class="card-name">Daniel Fenwick</p>
      <p class="card-title">Managing Partner</p>
      <p class="card-company">Harborline Journey Services, Inc.</p>
      <p>274 Alder Lane, Suite 3621</p>
      <p>Calder Falls, ME 04990</p>
      <div class="card-gap"></div>
      <p>&#9742; 207-555-0148 (Direct)</p>
      <p>&#9632; 207-555-0193</p>
      <p>&#9993; daniel@harborlinejourney.net</p>
      <p>&#9679; www.harborlinejourney.net</p>
    </div>
  </section>

  <section class="piece card card-back" aria-label="Business card, back">
    <div class="brand brand--light"><span class="brand-dot"></span>HARBORLINE</div>
  </section>

  <section class="piece envelope envelope-front" aria-label="Envelope, front">
    <div class="brand"><span class="brand-dot"></span>HARBORLINE</div>
    <address class="return-address">
      <p class="company">Harborline Journey Services, Inc.</p>
      <p>274 Alder Lane, Suite 3621</p>
      <p>Calder Falls, ME 04990</p>
    </address>
  </section>

  <section class="piece envelope envelope-back" aria-label="Envelope, back">
    <svg class="envelope-flap" viewBox="0 0 327 56" preserveAspectRatio="none" aria-hidden="true">
      <path d="M0 0 H327 L320 52 Q319 56 314 56 H13 Q8 56 7 52 Z" fill="var(--blue)"/>
    </svg>
    <div class="brand brand--light"><span class="brand-dot"></span>HARBORLINE</div>
    <p class="flap-url">www.harborlinejourney.net</p>
  </section>

</body>
</html>
```